Flyer-Design für Immobilienmarketing von Raumfreude Home Staging
Zielgruppe
Wir (Raumfreude Home Staging) geben mit Home Staging Immobilien ein Raumfreude (www.raumfreude-beispiel.de). Ziel ist die Immobilienvermarktung zu beschleunigen (Immobilienmarketing) und den besten Preis zu erzielen. Durch ein eigenes Möbel und Dekolager erfolgt die Gestaltung zeitnah.
Zielgruppe sind Immobilienverkäufer (privat) und auch Makler/Vermittler/Projektentwickler
Aufgabenstellung
Wir benötigen einen Flyer/Klappkarte DIN lang quer. Dieser sollte hochwertig, einladend, hell und freundlich erscheinen. Wenn er an der langen Seite gefaltet ist, sollte er als Klappkarte auf dem Tisch stehen können. Dabei sollen alle 4 Seiten genutzt werden. Logo und Design sowie Kurzbeschreibungen/Texte entsprechend bitte der Website (www.raumfreude-beispiel.de) verwenden. Originale können zur Verfügung gestellt werden. Der Flyer sollte auch als PDF nutzbar sein.
Als Slogan stellen wir uns folgendes vor 'Mit Raumfreude in den Immobilienverkauf starten und beim besten Preis landen', sind aber für alles offen. Bei Verwendung von Referenzen wäre ein Spruch mit 'Wohlfühlen' gut. Des Weiteren einfach bei den Texten und Bildern der Website bedienen (Vorteile + warum mit uns) und einen knackigen überzeugenden Flyer bei dem hauptsächlich die Bilder sprechen, erstellen. Wir freuen uns auf die Vorschläge.

```html
<!DOCTYPE html>
<html lang="de">
<head>
<meta charset="utf-8">
<title>Raumfreude Home Staging – Klappkarte</title>
<link href="https://fonts.googleapis.com/css2?family=Questrial&family=Raleway:wght@400;600&display=swap" rel="stylesheet">
<style>
  :root{
    --page:#f3f3f3;
    --paper:#ffffff;
    --green:#95c11f;
    --ink:#3a3a3a;
    --muted:#7a7a7a;
    --wood:#b08a63;
    --cream:#e9e2d8;
    --linen:#d9d1c6;
    --teal:#2f6f74;
    --brick:#9a5b42;
    --sky:#cfe0ee;
  }
  *{box-sizing:border-box;margin:0;padding:0}
  html,body{width:891px;height:1200px;overflow:hidden;background:var(--page)}
  body{font-family:"Raleway",sans-serif;color:var(--ink);position:relative}

  .panel{position:absolute;background:var(--paper);box-shadow:0 3px 10px rgba(0,0,0,.18);overflow:hidden}
  .photo{position:absolute;display:block}

  /* photo tones */
  .t-living{background:linear-gradient(160deg,#f1ede7 0%,#d8cbbb 55%,#8a6d52 100%)}
  .t-fire{background:linear-gradient(160deg,#eeeae5 0%,#cdbfae 45%,var(--brick) 70%,#6e5240 100%)}
  .t-study{background:linear-gradient(160deg,#f6f4f0 0%,#e0d7cb 55%,#7d6550 100%)}
  .t-bed{background:linear-gradient(150deg,#f4f0ec 0%,#e4d9d2 50%,#b99d87 100%)}
  .t-teal{background:linear-gradient(150deg,var(--teal) 0%,#3f7f84 45%,#e8e0d8 70%,#c7a57f 100%)}
  .t-kitchen{background:linear-gradient(160deg,#f7f6f3 0%,#dcd5cc 60%,#a4876a 100%)}
  .t-dining{background:linear-gradient(160deg,#ecebe8 0%,#b9b6b1 50%,#6f6c68 100%)}
  .t-terrace{background:linear-gradient(180deg,var(--sky) 0%,#b9c3c9 45%,#6d5448 100%)}
  .t-store{background:linear-gradient(160deg,#dcd8d0 0%,#a7a093 50%,#5f584d 100%)}
  .t-house{background:linear-gradient(180deg,#8fc1e6 0%,#bcd9ec 40%,#7b8c96 70%,#6b8e4e 100%)}
  .t-lounge{background:linear-gradient(160deg,#efebe6 0%,#d3c6b8 55%,#97826e 100%)}

  .green-bar{position:absolute;background:var(--green)}

  /* brand lockup */
  .brand{position:absolute;display:flex;align-items:center;gap:8px;color:var(--ink);font-family:"Questrial",sans-serif}
  .brand-mark{width:10px;height:10px;background:var(--green);flex:none}
  .brand-name{line-height:1;letter-spacing:.5px}
  .brand-name small{display:block;font-size:.38em;letter-spacing:2px;text-transform:uppercase;margin-top:3px;text-align:right}

  /* front */
  .front{left:115px;top:80px;width:660px;height:314px}
  .front .band{position:absolute;left:0;top:186px;width:660px;height:70px}
  .front .brand{left:70px;top:15px}
  .front .brand-name{font-size:31px}
  .front .slogan{position:absolute;left:345px;top:19px;font-family:"Questrial",sans-serif;font-size:13px;line-height:18px;padding-left:13px}
  .front .slogan .green-bar{left:0;top:2px;width:5px;height:33px}

  /* inside spread */
  .spread{left:10px;top:444px;width:871px;height:207px}
  .spread .fold{position:absolute;left:435px;top:0;width:1px;height:207px;background:#dedede}
  .benefit{position:absolute;top:96px;width:190px;padding-left:8px}
  .benefit .green-bar{left:0;top:1px;width:4px;height:59px}
  .benefit h2{font-size:8.6px;font-weight:600;color:var(--muted);line-height:10px}
  .benefit p{font-size:6.4px;line-height:10.2px;margin-top:1px}

  /* back */
  .back{left:115px;top:701px;width:660px;height:314px}
  .back .claim{position:absolute;left:22px;top:142px;font-family:"Questrial",sans-serif;font-size:11.5px;line-height:19px;color:#fff;padding-left:8px;text-shadow:0 1px 2px rgba(0,0,0,.35)}
  .back .claim .green-bar{left:0;top:2px;width:3px;height:34px;background:#fff}
  .back .brand{left:388px;top:82px}
  .back .brand-name{font-size:28px}
  .contact{position:absolute;left:528px;top:140px;font-size:8.6px;line-height:15.6px;color:var(--muted)}
  .contact .person{font-style:italic}
  .contact .web{font-weight:600;color:var(--ink)}
</style>
</head>
<body>

<!-- Title page -->
<section class="panel front" aria-label="Titelseite">
  <div class="photo t-living" style="left:0;top:0;width:142px;height:186px" role="img" aria-label="Wohnzimmer mit Sessel und Beistelltisch"></div>
  <div class="photo t-fire" style="left:148px;top:0;width:290px;height:186px" role="img" aria-label="Wohnraum mit Kamin und Sofa"></div>
  <div class="photo t-study" style="left:444px;top:0;width:216px;height:186px" role="img" aria-label="Arbeitsecke mit Regal und Schreibtisch"></div>

  <div class="band">
    <div class="brand">
      <span class="brand-mark"></span>
      <span class="brand-name">raumfreude<small>Home Staging</small></span>
    </div>
    <p class="slogan"><span class="green-bar"></span>Wir geben Immobilien den perfekten Look<br>für einen erfolgreichen Verkauf.</p>
  </div>

  <div class="photo t-bed" style="left:0;top:256px;width:142px;height:58px" role="img" aria-label="Schlafzimmer"></div>
  <div class="photo t-kitchen" style="left:148px;top:256px;width:68px;height:58px" role="img" aria-label="Flur"></div>
  <div class="photo t-dining" style="left:222px;top:256px;width:142px;height:58px" role="img" aria-label="Essbereich"></div>
  <div class="photo t-lounge" style="left:370px;top:256px;width:142px;height:58px" role="img" aria-label="Wohnbereich"></div>
  <div class="photo t-bed" style="left:518px;top:256px;width:142px;height:58px" role="img" aria-label="Ankleide mit Bett"></div>
</section>

<!-- Inside spread -->
<section class="panel spread" aria-label="Innenseiten">
  <div class="photo t-teal" style="left:0;top:0;width:142px;height:80px" role="img" aria-label="Schlafzimmer mit petrolfarbener Wand"></div>
  <div class="photo t-fire" style="left:146px;top:0;width:142px;height:80px" role="img" aria-label="Wohnraum mit Kamin und Lesesessel"></div>
  <div class="photo t-study" style="left:292px;top:0;width:143px;height:80px" role="img" aria-label="Arbeitsecke mit Regal"></div>
  <div class="photo t-dining" style="left:436px;top:0;width:142px;height:80px" role="img" aria-label="Offene Küche mit Essbereich"></div>
  <div class="photo t-living" style="left:582px;top:0;width:142px;height:80px" role="img" aria-label="Wohnzimmer mit Sofa"></div>
  <div class="photo t-terrace" style="left:728px;top:0;width:143px;height:80px" role="img" aria-label="Dachterrasse mit Essgruppe"></div>

  <div class="fold"></div>

  <article class="benefit" style="left:49px">
    <span class="green-bar"></span>
    <h2>Sie wecken das<br>größte Interesse</h2>
    <p>Wir setzen Ihre Immobilie mit den pas-<br>senden Möbeln für den Verkauf gekonnt<br>in Szene und wecken mit professionellen<br>Immobilienfotos das größte Kaufinteresse.</p>
  </article>
  <article class="benefit" style="left:244px">
    <span class="green-bar"></span>
    <h2>Sie erzielen den<br>besten Preis</h2>
    <p>Mit unserem hochwertigen Home Staging<br>machen wir den Wert Ihrer Immobilie<br>sichtbar und zeigen das Potential auf. So<br>erzielen Sie den besten Preis.</p>
  </article>
  <article class="benefit" style="left:488px">
    <span class="green-bar"></span>
    <h2>Sie sparen viel<br>Zeit und Nerven</h2>
    <p>Unser Ziel ist eine kurze Vermarktungszeit<br>Ihrer Immobilie. Damit sparen Sie die wei-<br>teren laufenden Kosten der Immobilie und<br>verringern die Anzahl der Besichtigungen.</p>
  </article>
  <article class="benefit" style="left:683px">
    <span class="green-bar"></span>
    <h2>Sie finden schnell<br>einen Käufer</h2>
    <p>Kaufinteressenten wollen sich in ihr zu-<br>künftiges Zuhause sofort verlieben. Mit un-<br>serem Raumfreude fällt die Entscheidung<br>für Ihre Immobilie ganz leicht und schnell.</p>
  </article>

  <div class="photo t-kitchen" style="left:0;top:169px;width:84px;height:38px" role="img" aria-label="Essplatz"></div>
  <div class="photo t-kitchen" style="left:88px;top:169px;width:92px;height:38px" role="img" aria-label="Küche"></div>
  <div class="photo t-lounge" style="left:184px;top:169px;width:58px;height:38px" role="img" aria-label="Balkontür"></div>
  <div class="photo t-study" style="left:246px;top:169px;width:94px;height:38px" role="img" aria-label="Flur"></div>
  <div class="photo t-bed" style="left:344px;top:169px;width:91px;height:38px" role="img" aria-label="Kinderzimmer"></div>
  <div class="photo t-living" style="left:436px;top:169px;width:92px;height:38px" role="img" aria-label="Wohnzimmer"></div>
  <div class="photo t-study" style="left:532px;top:169px;width:46px;height:38px" role="img" aria-label="Eingang"></div>
  <div class="photo t-dining" style="left:582px;top:169px;width:92px;height:38px" role="img" aria-label="Wohnbereich"></div>
  <div class="photo t-kitchen" style="left:678px;top:169px;width:96px;height:38px" role="img" aria-label="Essbereich"></div>
  <div class="photo t-lounge" style="left:778px;top:169px;width:93px;height:38px" role="img" aria-label="Schlafbereich"></div>
</section>

<!-- Back page -->
<section class="panel back" aria-label="Rückseite">
  <div class="photo t-lounge" style="left:0;top:0;width:363px;height:186px" role="img" aria-label="Wohnzimmer mit Sesseln, Sofa und Wandbild"></div>
  <p class="claim"><span class="green-bar"></span>Mit Raumfreude in den Immobilienverkauf starten<br>und beim besten Preis landen</p>
  <div class="photo t-store" style="left:0;top:192px;width:142px;height:122px" role="img" aria-label="Möbel- und Dekolager mit Regalen"></div>
  <div class="photo t-house" style="left:148px;top:192px;width:215px;height:122px" role="img" aria-label="Lagergebäude mit Firmenwagen"></div>

  <div class="brand">
    <span class="brand-mark"></span>
    <span class="brand-name">raumfreude<small>Home Staging</small></span>
  </div>
  <address class="contact" style="font-style:normal">
    <span class="person" style="font-style:italic">Lena Brandt-Vogel</span><br>
    Lindenstieg 14b<br>
    22000 Hamburg<br>
    Tel.: 040 / 123 456 78<br>
    info@raumfreude-beispiel.de<br>
    <span class="web">www.raumfreude-beispiel.de</span>
  </address>
</section>

</body>
</html>
```